Beyond The Ledger Double Sided DL Flyer

We need a double sided flyer that we provide to a Real Estate agent for leeds. It should provide our basic services as well as a modern look and feel. The brochure should incorporate our Brand colors and have a graphic that centres around money and property. I have included a couple of pictures that we like (but have not yet purchased from PIXVAULT) as an indication of the type of picture we like.

WE need to also show the Beyond The Ledger brand and have our Phone / address's and email details.

Target Market(s)

Realestate clients (Property Investors)

Industry/Entity Type

Financial Planning

Requirements
Must have
• Picture on Front (maybe the logo on back)
• Please incorporate existing logo colours.

```html
<!DOCTYPE html>
<html lang="en">
<head>
<meta charset="utf-8">
<title>Beyond The Ledger – DL Flyer</title>
<link rel="stylesheet" href="https://fonts.googleapis.com/css2?family=Open+Sans:wght@300;400;600;700&display=swap">
<style>
  :root {
    --brand-green: #8dc63f;
    --brand-green-soft: rgba(141, 198, 63, 0.55);
    --ink: #231f20;
    --body-text: #444444;
    --paper: #ffffff;
    --backdrop: #dcdcdc;
    --bar-grey: #4a4a4a;
  }
  * { box-sizing: border-box; margin: 0; padding: 0; }
  html, body {
    width: 1200px; height: 803px; overflow: hidden;
    background: var(--backdrop);
    font-family: "Open Sans", Arial, sans-serif;
    color: var(--ink);
  }
  .canvas { position: relative; width: 1200px; height: 803px; }

  .flyer-page {
    position: absolute;
    width: 303px; height: 637px;
    background: var(--paper);
    transform: scale(0.92);
    transform-origin: 0 0;
    overflow: hidden;
  }
  .flyer-page--front { left: 304px; top: 106px; }
  .flyer-page--back { left: 646px; top: 110px; }

  .brand {
    position: absolute; left: 30px; top: 38px; width: 250px;
  }
  .brand-row { display: flex; align-items: center; gap: 8px; }
  .brand-square { width: 14px; height: 14px; background: var(--brand-green); flex: none; }
  .brand-name {
    font-size: 21px; font-weight: 700; color: var(--ink);
    letter-spacing: 0.2px; line-height: 1;
  }

  .graphic { position: absolute; left: 0; top: 0; width: 303px; height: 637px; }

  .section-title {
    position: absolute; left: 0; width: 303px; text-align: center;
    font-size: 30px; font-weight: 700; color: var(--ink); letter-spacing: 0.3px;
  }
  .title-rule { position: absolute; height: 2px; background: var(--brand-green); }

  /* front */
  .services-title { top: 388px; }
  .services-rule { left: 89px; width: 125px; top: 430px; }
  .services-intro {
    position: absolute; left: 0; top: 443px; width: 303px; text-align: center;
    font-size: 18.5px; font-weight: 600; color: var(--brand-green); line-height: 24.5px;
  }
  .service-list { position: absolute; left: 28px; top: 503px; list-style: none; }
  .service-list li {
    position: relative; padding-left: 12px;
    font-size: 10.6px; color: var(--body-text); line-height: 22.6px;
  }
  .service-list li::before {
    content: ""; position: absolute; left: 0; top: 9px;
    width: 4px; height: 4px;
    border-right: 1.5px solid var(--brand-green); border-top: 1.5px solid var(--brand-green);
    transform: rotate(45deg);
  }
  .footer-bar {
    position: absolute; left: 27px; top: 626px; width: 248px; height: 11px;
    background: var(--brand-green);
  }

  /* back */
  .role-title {
    position: absolute; left: 30px; top: 106px;
    font-size: 31px; font-weight: 300; color: var(--ink); line-height: 39px;
  }
  .person-name {
    position: absolute; left: 30px; top: 190px;
    font-size: 27px; font-weight: 600; color: var(--brand-green);
  }
  .contact-title { top: 468px; }
  .contact-rule { left: 92px; width: 120px; top: 508px; }
  .contact-list { position: absolute; left: 34px; top: 524px; list-style: none; }
  .contact-item { display: flex; align-items: flex-start; gap: 14px; margin-bottom: 10px; }
  .contact-icon { width: 14px; height: 14px; flex: none; margin-top: 1px; }
  .contact-text { font-size: 10.6px; color: var(--body-text); line-height: 12.8px; }
</style>
</head>
<body>
<main class="canvas">

  <!-- Front: services -->
  <section class="flyer-page flyer-page--front">
    <header class="brand">
      <div class="brand-row">
        <span class="brand-square"></span>
        <span class="brand-name">Beyond The Ledger</span>
      </div>
    </header>

    <svg class="graphic" viewBox="0 0 303 637">
      <defs>
        <linearGradient id="front-photo-tone" x1="0" y1="0" x2="1" y2="1">
          <stop offset="0" stop-color="#e9ddd0"/>
          <stop offset="0.5" stop-color="#c9b9a6"/>
          <stop offset="1" stop-color="#8fa979"/>
        </linearGradient>
      </defs>
      <polygon role="img" aria-label="Photo: hands holding a small wooden house beside stacks of coins with seedlings growing"
               points="0,140 289,103 289,312 0,355" fill="url(#front-photo-tone)"/>
      <polygon points="289,118 303,116 303,330 289,332" fill="var(--brand-green)"/>
      <rect x="0" y="130" width="49" height="45" fill="var(--brand-green-soft)"/>
      <polygon points="254,112 303,106 303,112 254,118" fill="var(--bar-grey)"/>
      <polygon points="0,355 303,310 303,335 0,390" fill="var(--brand-green)"/>
      <polygon points="0,350 41,344 41,351 0,357" fill="var(--bar-grey)"/>
    </svg>

    <h2 class="section-title services-title">SERVICES</h2>
    <div class="title-rule services-rule"></div>
    <p class="services-intro">Accountants and Financial<br>Advisors who specialise in</p>
    <ul class="service-list">
      <li>Negative Gearing &amp; Investment Properties</li>
      <li>Property &amp; Capital Gains Tax Minimisation</li>
      <li>Self-Managed Superannuation Funds (SMSF)</li>
      <li>Small Business &amp; Personal Taxation</li>
      <li>Investment Advice &amp; Risk Insurances</li>
    </ul>
    <div class="footer-bar"></div>
  </section>

  <!-- Back: contact -->
  <section class="flyer-page flyer-page--back">
    <header class="brand">
      <div class="brand-row">
        <span class="brand-square"></span>
        <span class="brand-name">Beyond The Ledger</span>
      </div>
    </header>

    <h1 class="role-title">ADVISOR /<br>ACCOUNTANT</h1>
    <p class="person-name">Paul Hartley</p>

    <svg class="graphic" viewBox="0 0 303 637">
      <defs>
        <linearGradient id="back-photo-tone" x1="0" y1="0" x2="0" y2="1">
          <stop offset="0" stop-color="#3f7a2c"/>
          <stop offset="0.6" stop-color="#6d9a48"/>
          <stop offset="1" stop-color="#9a7a55"/>
        </linearGradient>
      </defs>
      <polygon role="img" aria-label="Photo: watering can sprinkling a seedling in a coin jar beside a small dark house and coin stacks"
               points="19,300 303,225 303,430 19,430" fill="url(#back-photo-tone)"/>
      <polygon points="8,318 19,315 19,430 8,430" fill="var(--brand-green)"/>
      <rect x="8" y="430" width="295" height="23" fill="var(--brand-green)"/>
      <polygon points="0,428 40,422 40,426 0,432" fill="var(--bar-grey)"/>
    </svg>

    <h2 class="section-title contact-title">CONTACT US</h2>
    <div class="title-rule contact-rule"></div>
    <ul class="contact-list">
      <li class="contact-item">
        <svg class="contact-icon" viewBox="0 0 14 14" aria-hidden="true">
          <path d="M7 0.5C4.5 0.5 2.6 2.4 2.6 4.9 2.6 8.2 7 13.5 7 13.5S11.4 8.2 11.4 4.9C11.4 2.4 9.5 0.5 7 0.5Z M7 6.6A1.7 1.7 0 1 1 7 3.2 1.7 1.7 0 0 1 7 6.6Z" fill="var(--ink)" fill-rule="evenodd"/>
        </svg>
        <p class="contact-text">8 / 112 Harbour View Rd Kelston NSW 2251<br>2 / 19 Lakeside Pde Marlow NSW 2264<br>(By Appointment)</p>
      </li>
      <li class="contact-item">
        <svg class="contact-icon" viewBox="0 0 14 14" aria-hidden="true">
          <path d="M3.2 1C2.4 1 1.2 2 1.3 3.3 1.6 7.8 6.2 12.4 10.7 12.7 12 12.8 13 11.6 13 10.8L10.6 8.9 8.9 10.2C7 9.3 4.7 7 3.8 5.1L5.1 3.4Z" fill="var(--ink)"/>
        </svg>
        <p class="contact-text">(02) 43015566</p>
      </li>
      <li class="contact-item">
        <svg class="contact-icon" viewBox="0 0 14 14" aria-hidden="true">
          <rect x="1" y="3" width="12" height="8.5" fill="var(--ink)"/>
          <path d="M1.5 3.5L7 7.8 12.5 3.5" stroke="#fff" stroke-width="1.1" fill="none"/>
        </svg>
        <p class="contact-text">info@beyondtheledger.com.au</p>
      </li>
    </ul>
    <div class="footer-bar"></div>
  </section>

</main>
</body>
</html>
```